Retail Appliance Store Chain needs NEW business Card

Name of my company is Brennan's Appliances brennansappliances.example is our website. . We are a 2 location brick and mortar, and online store selling premium, luxury, and normal household appliances, such as ovens, stoves, cooktops, dishwashers, refrigerators, washers and dryers, grills, air conditioners etc. The focus is on large kitchen appliances and laundry appliances.
Please visit http://brennansappliances.example to get a feel for the business and branding.
I have attached the Brennan's Appliances logo (i do not have eps or psd or ai). And I have also attached our current business cards that we use. We have two versions. A double sided version for managers, and a one side version for regular employees.
Please submit BOTH one sided and two sided designs if possible.
Please keep consistent with the Brennan's Appliances logo, colors, etc.
I would prefer no rounded corners on the business card designs for printing costs.
Information on the cards (in no particular order):
Name - Employee Name
Business name - Brennan's Appliances
website - brennansappliances.example
Email - Employee Email
2 Phone Numbers - store 1 address, store 2 address
2 Addresses - store 1 address, store 2 address

*do NOT need Fax #

Industry/Entity Type

Home Appliance

Contact Information for Business Card

Logo - Brennans Appliances Logo
Name - Employee Name
Email - Employee Email

Please no rounded corners. Standard US Business Card Size please.

Font styles to use
Serif
Sans Serif

Requirements
Must have
• colors and design that somewhat match the feel of current logo and website
Should not have
• No rounded corners.
No non-traditional business card size. US Standard Business Card Size only

```html
<!DOCTYPE html>
<html lang="en">
<head>
<meta charset="utf-8">
<title>Brennan's Appliances – Business Cards</title>
<link rel="stylesheet" href="https://fonts.googleapis.com/css2?family=Open+Sans:wght@400;600;700&display=swap">
<style>
  :root {
    --navy: #1e1b4f;
    --navy-deep: #161340;
    --gold-dark: #7a4a16;
    --gold: #b8801f;
    --gold-bright: #f2c313;
    --white: #ffffff;
    --stage: #2b2d30;
  }
  html, body {
    margin: 0;
    width: 1200px;
    height: 900px;
    overflow: hidden;
    background: var(--stage);
    font-family: "Open Sans", Arial, sans-serif;
  }
  .sheet {
    width: 1200px;
    height: 900px;
    display: flex;
    flex-direction: column;
    align-items: center;
    justify-content: center;
    gap: 40px;
  }
  .card {
    width: 640px;
    height: 366px;
    display: block;
    box-shadow: 0 12px 30px rgba(0,0,0,.45);
  }
  .brand-name { font-family: "Open Sans", Arial, sans-serif; font-weight: 700; fill: var(--white); }
  .brand-caps { font-family: "Open Sans", Arial, sans-serif; font-weight: 600; fill: var(--white); letter-spacing: 3px; }
  .web { font-family: "Open Sans", Arial, sans-serif; font-weight: 400; fill: var(--white); letter-spacing: 1px; }
  .contact { font-family: "Open Sans", Arial, sans-serif; font-weight: 400; fill: var(--white); font-size: 13px; }
  .person-name { font-family: "Open Sans", Arial, sans-serif; fill: var(--white); font-size: 26px; }
  .person-role { font-family: "Open Sans", Arial, sans-serif; fill: var(--white); font-size: 13px; }
</style>
</head>
<body>
<main class="sheet">

  <!-- Front: brand side -->
  <svg class="card card-front" viewBox="0 0 640 366" xmlns="http://www.w3.org/2000/svg" aria-label="Business card front">
    <defs>
      <linearGradient id="front-gold" x1="0" y1="0" x2="1" y2="0">
        <stop offset="0" stop-color="var(--gold-dark)"/>
        <stop offset="0.45" stop-color="var(--gold-bright)"/>
        <stop offset="1" stop-color="var(--gold-dark)"/>
      </linearGradient>
    </defs>
    <rect class="front-base" width="640" height="366" fill="var(--navy)"/>
    <path class="front-gold-band" role="img" aria-label="Gold band with decorative flowing lines"
          d="M0 110 C120 110 200 150 260 210 C290 240 350 240 380 210 C440 150 520 110 640 110 V366 H0 Z" fill="url(#front-gold)"/>
    <path class="front-edge-line" d="M0 100 C120 100 200 140 260 200 C290 230 350 230 380 200 C440 140 520 100 640 100" fill="none" stroke="var(--navy-deep)" stroke-width="4"/>
    <text class="brand-name" x="320" y="62" font-size="30" text-anchor="middle">Brennan's Appliances</text>
    <text class="brand-caps" x="320" y="92" font-size="15" text-anchor="middle">BRENNAN'S APPLIANCES</text>
    <text class="web" x="320" y="330" font-size="15" text-anchor="middle">www.brennansappliances.example</text>
  </svg>

  <!-- Back: contact side -->
  <svg class="card card-back" viewBox="0 0 640 366" xmlns="http://www.w3.org/2000/svg" aria-label="Business card back">
    <defs>
      <linearGradient id="back-gold" x1="0" y1="0" x2="1" y2="0">
        <stop offset="0" stop-color="var(--gold-dark)"/>
        <stop offset="0.5" stop-color="var(--gold-bright)"/>
        <stop offset="1" stop-color="var(--gold-dark)"/>
      </linearGradient>
      <linearGradient id="icon-gold" x1="0" y1="0" x2="1" y2="1">
        <stop offset="0" stop-color="var(--gold-bright)"/>
        <stop offset="1" stop-color="var(--gold-dark)"/>
      </linearGradient>
    </defs>
    <rect class="back-base" width="640" height="366" fill="var(--navy)"/>
    <path class="back-white-edge" d="M0 130 C80 134 140 170 230 180 C330 190 420 150 500 170 C560 185 610 200 640 205 V214 C600 210 560 196 500 180 C420 160 330 200 230 190 C140 180 80 146 0 142 Z" fill="var(--white)"/>
    <path class="back-gold-band" role="img" aria-label="Gold band with decorative flowing lines"
          d="M0 0 H640 V200 C610 196 560 182 500 166 C420 146 330 186 230 176 C140 166 80 130 0 126 Z" fill="url(#back-gold)"/>

    <text class="brand-name" x="32" y="52" font-size="24">Brennan's Appliances</text>
    <text class="brand-caps" x="32" y="80" font-size="13">BRENNAN'S APPLIANCES</text>

    <g class="person" transform="translate(420 70)">
      <circle r="14" fill="var(--white)"/>
      <circle cy="-4" r="4.5" fill="var(--gold)"/>
      <path d="M-8 9 C-8 1 8 1 8 9 Z" fill="var(--gold)"/>
      <text class="person-name" x="24" y="9"><tspan font-weight="700">Lorem</tspan> ipsum</text>
      <text class="person-role" x="110" y="32">Designer</text>
    </g>

    <g class="contacts contacts-left" transform="translate(32 222)">
      <g class="contact-row">
        <circle r="12" fill="url(#icon-gold)"/>
        <circle r="6" fill="none" stroke="var(--navy)" stroke-width="1.3"/>
        <path d="M-6 0 H6 M0 -6 V6" stroke="var(--navy)" stroke-width="1.1"/>
        <text class="contact" x="22" y="5">www.brennansappliances.example</text>
      </g>
      <g class="contact-row" transform="translate(0 36)">
        <circle r="12" fill="url(#icon-gold)"/>
        <path d="M-5 -6 C-7 -2 -2 6 4 6 L6 3 L3 1 L1 2 C-1 1 -2 -1 -2 -3 L-1 -5 L-3 -7 Z" fill="var(--navy)"/>
        <text class="contact" x="22" y="5">+77 7777 7777 7773</text>
      </g>
      <g class="contact-row" transform="translate(0 72)">
        <circle r="12" fill="url(#icon-gold)"/>
        <path d="M-6 0 L0 -6 L6 0 V6 H-6 Z" fill="var(--navy)"/>
        <text class="contact" x="22" y="0">Street Address Here</text>
        <text class="contact" x="22" y="17">Italy, 2222</text>
      </g>
      <path d="M22 16 H210 M22 52 H210" stroke="var(--gold)" stroke-width="1"/>
    </g>

    <g class="contacts contacts-right" transform="translate(380 232)">
      <g class="contact-row">
        <circle r="12" fill="url(#icon-gold)"/>
        <path d="M-6 1 L6 -6 L2 6 L0 2 Z" fill="var(--navy)"/>
        <text class="contact" x="22" y="5">username@email.com</text>
      </g>
      <g class="contact-row" transform="translate(0 36)">
        <circle r="12" fill="url(#icon-gold)"/>
        <path d="M-5 -6 C-7 -2 -2 6 4 6 L6 3 L3 1 L1 2 C-1 1 -2 -1 -2 -3 L-1 -5 L-3 -7 Z" fill="var(--navy)"/>
        <text class="contact" x="22" y="5">+77 7777 7777 7723</text>
      </g>
      <g class="contact-row" transform="translate(0 72)">
        <circle r="12" fill="url(#icon-gold)"/>
        <path d="M-6 0 L0 -6 L6 0 V6 H-6 Z" fill="var(--navy)"/>
        <text class="contact" x="22" y="0">Street Address Here</text>
        <text class="contact" x="22" y="17">Italy, 2222</text>
      </g>
      <path d="M22 16 H220 M22 52 H220" stroke="var(--gold)" stroke-width="1"/>
    </g>
  </svg>

</main>
</body>
</html>
```